Steadfast MD - Sleep Medicine Specialist - Business Cards

We are a new medical practice called Steadfast MD. We are sleep medicine specialists and we will be conducting sleep studies on patients with sleep related ailments. We want the business card to be bold, professional, and clean with the logo as the stand out visual piece. We dont like wild flashy designs. We want our design to be bold and classic while at the same time conveying who we are and what we do. We are reliable, professional, and the best in the business.

Industry/Entity Type

Health Care

Contact Information for Business Card

- Clean
- Bold
- Classic
- not cluttered

Requirements
Must have
• logo, website, phone number
Nice to have
• several options to choose from
Should not have
• flashy imaged - reflective print - images of people sleeping

```html
<!DOCTYPE html>
<html lang="en">
<head>
<meta charset="utf-8">
<title>Steadfast MD – Business Card</title>
<link rel="stylesheet" href="https://fonts.googleapis.com/css2?family=Poppins:wght@400;500;700;800&display=swap">
<style>
  :root {
    --brand-red: #e10000;
    --brand-red-deep: #c00000;
    --ink: #161616;
    --ink-soft: #3a3a3a;
    --stage: #d9d6d1;
    --white: #ffffff;
  }
  * { box-sizing: border-box; margin: 0; padding: 0; }
  html, body {
    width: 1200px; height: 780px; overflow: hidden;
    background: var(--stage);
    font-family: "Poppins", sans-serif;
  }
  .canvas {
    position: relative; width: 1200px; height: 780px;
    display: flex; flex-direction: column; align-items: center; justify-content: center; gap: 40px;
  }
  .card {
    position: relative; width: 600px; height: 343px;
    border-radius: 18px; overflow: hidden;
    box-shadow: 0 10px 28px rgba(0,0,0,0.22);
  }
  .card-art { position: absolute; inset: 0; width: 100%; height: 100%; display: block; }

  /* Front */
  .holder { position: absolute; top: 18px; right: 30px; text-align: right; color: var(--white); }
  .holder-name { font-weight: 700; font-size: 17px; letter-spacing: 0.3px; line-height: 1.1; }
  .holder-role { font-weight: 400; font-size: 13px; line-height: 1.2; }

  .brand { position: absolute; display: flex; align-items: center; gap: 14px; white-space: nowrap; }
  .brand-mark { border-radius: 50%; flex: none; }
  .brand-name { font-weight: 800; line-height: 1; letter-spacing: -0.5px; }

  .front .brand { left: 90px; top: 192px; }
  .front .brand-mark { width: 56px; height: 56px; border: 4px solid var(--brand-red); }
  .front .brand-name { font-size: 40px; color: var(--ink); }

  .contact-list { position: absolute; left: 90px; top: 266px; list-style: none; }
  .contact-list li {
    display: flex; align-items: center; gap: 8px;
    font-size: 14px; color: var(--ink-soft); line-height: 21px;
  }
  .contact-icon { width: 16px; height: 16px; flex: none; }

  .address {
    position: absolute; left: 388px; top: 274px;
    font-size: 14px; line-height: 21px; font-style: normal; color: var(--ink-soft);
  }

  /* Back */
  .back { background: linear-gradient(135deg, var(--brand-red) 0%, var(--brand-red-deep) 100%); }
  .back .brand { left: 50%; top: 50%; transform: translate(-50%, -50%); }
  .back .brand-mark { width: 62px; height: 62px; border: 4px solid var(--white); }
  .back .brand-name { font-size: 46px; color: var(--white); }
</style>
</head>
<body>
<main class="canvas">

  <section class="card front" aria-label="Business card, front">
    <svg class="card-art" viewBox="0 0 600 343" aria-hidden="true">
      <defs>
        <linearGradient id="paperShade" x1="0" y1="0" x2="1" y2="1">
          <stop offset="0" stop-color="#fafafa"/>
          <stop offset="1" stop-color="#e2e2e2"/>
        </linearGradient>
      </defs>
      <rect width="600" height="343" fill="url(#paperShade)"/>
      <path d="M0 0 H600 V78 C380 92 170 150 0 240 Z" fill="#e10000"/>
      <path d="M0 240 C170 150 380 92 600 78 V92 C380 104 170 162 0 250 Z" fill="#161616"/>
      <line x1="60" y1="258" x2="560" y2="258" stroke="#e10000" stroke-width="1.2"/>
      <line x1="368" y1="272" x2="368" y2="322" stroke="#e10000" stroke-width="1.2"/>
    </svg>

    <div class="holder">
      <p class="holder-name">OWEN HARTLEY</p>
      <p class="holder-role">Manager</p>
    </div>

    <div class="brand">
      <span class="brand-mark"></span>
      <span class="brand-name">Steadfast MD</span>
    </div>

    <ul class="contact-list">
      <li>
        <svg class="contact-icon" viewBox="0 0 16 16" aria-hidden="true">
          <circle cx="8" cy="8" r="8" fill="#e10000"/>
          <path d="M5.2 4.2 L6.6 4 L7.3 5.8 L6.4 6.5 C6.9 7.7 8.3 9.1 9.5 9.6 L10.2 8.7 L12 9.4 L11.8 10.8 C8.4 11.2 4.8 7.6 5.2 4.2 Z" fill="#fff"/>
        </svg>
        +1 555 204 3817
      </li>
      <li>
        <svg class="contact-icon" viewBox="0 0 16 16" aria-hidden="true">
          <circle cx="8" cy="8" r="8" fill="#e10000"/>
          <rect x="4" y="5.2" width="8" height="5.6" rx="0.6" fill="none" stroke="#fff" stroke-width="1.1"/>
          <path d="M4.2 5.6 L8 8.4 L11.8 5.6" fill="none" stroke="#fff" stroke-width="1.1"/>
        </svg>
        care@steadfastmd.com
      </li>
      <li>
        <svg class="contact-icon" viewBox="0 0 16 16" aria-hidden="true">
          <circle cx="8" cy="8" r="8" fill="#e10000"/>
          <circle cx="8" cy="8" r="4" fill="none" stroke="#fff" stroke-width="1.1"/>
          <ellipse cx="8" cy="8" rx="1.7" ry="4" fill="none" stroke="#fff" stroke-width="1"/>
          <line x1="4" y1="8" x2="12" y2="8" stroke="#fff" stroke-width="1"/>
        </svg>
        www.steadfastmd.com
      </li>
    </ul>

    <address class="address">
      PO BOX 418, Linden Avenue<br>
      Ashgrove, Victoria
    </address>
  </section>

  <section class="card back" aria-label="Business card, back">
    <div class="brand">
      <span class="brand-mark"></span>
      <span class="brand-name">Steadfast MD</span>
    </div>
  </section>

</main>
</body>
</html>
```